Copper Vale Mailer 2.6.2018

We are a multifaceted waste solutions company, handling residential & commercial solid waste management. Residential is the small yellow dumpsters & the small black trash cans. Mention start up specials somewhere. The Roll-off is part of the commercial waste hauling, includes the huge black commercial dumpsters.

Septic pumping (liquid waste)

We are Locally Owned & Family Operated which is critical to mention in this area! ****We have new competitors who are posing as small locally owned companies, but they are actually huge corporations. “wolves in sheep clothing”. I need to make this a point on the card somehow. Please help me be creative. Pointing people to us, a local business.
We are a charitable business, who donates monthly to local non-profits.
Bilingual: English & Spanish please include the phrase  “Se Habla Español” in red on both sides.
Always show our 5 star reviews on searchly, chatterpage, and marla's roster.
We support America and our troops, flags are always a nice touch.
-------------------------------------------------------------------------------------------
For septic side: Military, senior, clerical and seasonal discounts. 24/7 septic emergency response (make a focus of this). We perform electronic tank location services, camera snaking, emergency septic repairs, Real estate septic inspections. free over the phone quotes. 12 month supply of Septic pills available for purchase 1 box for $55 or two for $95 (see photo of pill boxes).
--------------------------------------------------------------------------------------------
For Trash: Military, senior, clerical & seasonal discounts. Scheduled bulk item removal services, whether a customer or not. Start up service specials.
No contracts
No hidden fees,
No admin fees
No fuel surcharges,
No eco fees,
Online billing available.
Roll-off: 24/hr turn around, reliable, etc. simple billing
Find additional information & photos on:
www.coppervalewaste.example
www.coppervaleseptic.example
https://www.chatterpage.example/coppervalewaste/
https://www.chatterpage.example/coppervaleseptic/

fbed22
000000
ffffff
ec1f27

• - Searchly & Marla's roster Ratings buttons
• - Photos (please clean them up as best as possible, they were poorly taken)
• - One side trash & roll-off focused, the other side septic focused. Along with their respective content & photos.
• - Will be QRPX mailer, so on the back side please make room for it.
• - Must mention website www.coppervalewaste.example on the trash side of the flyer and www.coppervaleseptic.example on the septic side of the flyer.
• - phone number both sides large

```html
<!DOCTYPE html>
<html lang="en">
<head>
<meta charset="utf-8">
<title>Copper Vale Mailer</title>
<link href="https://fonts.googleapis.com/css2?family=Gelasio:ital,wght@0,400;0,600;0,700;1,500;1,600&family=Roboto+Condensed:wght@400;700&family=Arimo:wght@400;700&display=swap" rel="stylesheet">
<style>
  :root {
    --yellow: #fbed22;
    --black: #000000;
    --white: #ffffff;
    --red: #ec1f27;
    --backdrop: #d9d9d9;
    --serif: "Gelasio", Georgia, serif;
    --condensed: "Roboto Condensed", "Arial Narrow", sans-serif;
    --sans: "Arimo", Arial, sans-serif;
  }
  * { box-sizing: border-box; margin: 0; padding: 0; }
  html, body { width: 894px; height: 1200px; overflow: hidden; background: var(--backdrop); }
  .sheet { position: relative; width: 894px; height: 1200px; }
  .card-slot { position: absolute; left: 17px; width: 860px; height: 573px; box-shadow: 0 4px 14px rgba(0,0,0,.35); }
  .card-slot.front { top: 17px; }
  .card-slot.back { top: 610px; }
  .card { position: absolute; left: 0; top: 0; width: 900px; height: 600px; transform: scale(.95556); transform-origin: 0 0; overflow: hidden; }
  .abs { position: absolute; white-space: nowrap; }
  .photo { position: absolute; }

  /* ---------- Trash side ---------- */
  .front .card { background: var(--black); font-family: var(--serif); }
  .front .header { left: 0; top: 0; width: 900px; height: 150px; background: var(--black); }
  .brand-mark { left: 30px; top: 32px; width: 78px; height: 78px; border-radius: 50%; background: var(--yellow); }
  .brand-name { left: 132px; top: 28px; color: var(--yellow); font-size: 33px; line-height: 44px; font-weight: 400; }
  .years-seal { left: 378px; top: 32px; width: 96px; height: 96px; border-radius: 50%; border: 3px solid var(--white); background: var(--black); color: var(--white); text-align: center; font-family: var(--sans); }
  .years-seal .num { display: block; font-size: 34px; font-weight: 700; line-height: 34px; margin-top: 20px; }
  .years-seal .lbl { display: block; font-size: 10px; font-weight: 700; letter-spacing: 1px; }
  .tagline { right: 30px; top: 40px; text-align: right; }
  .tagline h2 { color: var(--yellow); font-size: 22px; font-weight: 400; line-height: 28px; }
  .tagline p { color: var(--white); font-size: 15px; line-height: 18px; }
  .rule-top { left: 0; top: 148px; width: 900px; height: 6px; background: var(--yellow); }
  .truck-photo { left: 205px; top: 154px; width: 695px; height: 272px; background: linear-gradient(160deg, #f3f3f0 0%, #dcdcd6 35%, #2a2a2a 55%, #1a1a1a 70%, #e6c51a 85%, #f5d51e 100%); }
  .se-habla { color: var(--red); font-style: italic; font-weight: 600; font-size: 16px; }
  .front .se-habla { right: 30px; top: 164px; }
  .service-rail { left: 0; top: 150px; width: 212px; height: 410px; background: var(--yellow); }
  .service-photo { left: 15px; width: 195px; height: 105px; border: 3px solid var(--white); border-radius: 10px 10px 0 0; }
  .service-photo.cans { top: 134px; background: linear-gradient(135deg, #e9e9e6, #8a8d88 50%, #3c3f3b); }
  .service-photo.small-bin { top: 275px; background: linear-gradient(135deg, #eeeeee, #f2d81d 45%, #c9ad12); }
  .service-photo.roll-off { top: 408px; background: linear-gradient(135deg, #6a8c5a, #2b3a2c 50%, #9c7a55); }
  .service-label { left: 24px; font-family: var(--condensed); font-size: 15px; font-weight: 700; color: var(--black); }
  .service-label.l1 { top: 247px; }
  .service-label.l2 { top: 386px; }
  .service-label.l3 { top: 518px; }
  .spokesman { left: 182px; top: 372px; width: 138px; height: 188px; background: linear-gradient(180deg, #d8c7b0 0%, #c9d8e8 45%, #9fb3c9 100%); border-radius: 60px 60px 0 0; }
  .promo-band { left: 212px; top: 426px; width: 688px; height: 134px; background: var(--black); border-top: 5px solid var(--yellow); }
  .promo-copy { left: 300px; top: 437px; width: 300px; text-align: center; }
  .promo-copy .offer { color: var(--yellow); font-size: 17px; line-height: 22px; }
  .promo-copy .local { color: var(--white); font-size: 16px; line-height: 19px; margin-top: 8px; }
  .front-phone { left: 603px; top: 433px; color: var(--white); font-size: 35px; line-height: 42px; display: flex; align-items: center; gap: 8px; }
  .front-phone svg { width: 28px; height: 28px; fill: var(--white); }
  .front-web { left: 608px; top: 480px; color: var(--yellow); font-size: 17px; font-weight: 600; }
  .ratings { left: 600px; top: 510px; width: 290px; display: flex; justify-content: space-between; font-family: var(--sans); }
  .rating { display: flex; flex-direction: column; align-items: center; color: var(--white); }
  .rating .name { font-size: 14px; font-weight: 700; display: flex; align-items: center; gap: 4px; }
  .rating .name i { display: inline-block; width: 12px; height: 12px; background: var(--yellow); }
  .rating .stars { color: var(--yellow); font-size: 11px; letter-spacing: 1px; }
  .perks { left: 0; top: 560px; width: 900px; height: 32px; background: var(--yellow); display: flex; justify-content: space-between; align-items: center; font-style: italic; font-weight: 600; font-size: 14px; color: var(--black); padding: 0 12px; }
  .perks span { white-space: nowrap; }
  .perks span::before { content: "✓"; font-style: normal; margin-right: 2px; }

  /* ---------- Septic side ---------- */
  .back .card { background: var(--white); font-family: var(--serif); }
  .panel-shape { left: 0; top: 0; width: 520px; height: 600px; }
  .septic-mark { left: 26px; top: 30px; width: 58px; height: 58px; border-radius: 50%; background: var(--yellow); }
  .septic-name { left: 100px; top: 30px; color: var(--yellow); font-size: 28px; line-height: 31px; font-weight: 400; }
  .emergency { left: 330px; top: 22px; width: 96px; color: var(--white); text-align: center; font-family: var(--sans); font-style: italic; font-weight: 700; }
  .emergency .big { display: block; font-size: 38px; line-height: 40px; }
  .emergency .small { display: block; font-size: 12px; line-height: 12px; }
  .estimate-band { left: 0; top: 112px; width: 462px; height: 30px; background: var(--yellow); color: var(--black); font-size: 15px; line-height: 30px; padding-left: 16px; font-weight: 600; }
  .estimate-band em { margin-right: 12px; }
  .septic-truck { left: 0; top: 142px; width: 470px; height: 130px; background: linear-gradient(160deg, #5d6b4a 0%, #2a2a2a 40%, #1c1c1c 55%, #e8c81c 75%, #c9a918 100%); }
  .back .se-habla { left: 18px; top: 146px; }
  .thumb { top: 274px; width: 138px; height: 74px; border: 3px solid var(--white); border-radius: 10px; }
  .thumb.dig { left: 20px; background: linear-gradient(135deg, #9da886, #5b6a49); }
  .thumb.camera { left: 173px; background: linear-gradient(135deg, #9a8c76, #d9c025 50%, #5a4c3c); }
  .thumb.pills { left: 328px; background: linear-gradient(135deg, #e8ecf2, #2e4a86 55%, #1c2d55); }
  .septic-intro { left: 18px; top: 360px; width: 460px; color: var(--white); font-size: 14px; line-height: 18px; white-space: normal; }
  .septic-services { left: 26px; top: 410px; width: 440px; display: grid; grid-template-columns: 224px 1fr; row-gap: 5px; color: var(--white); font-size: 12.5px; }
  .septic-services li { list-style: none; display: flex; align-items: center; gap: 7px; }
  .septic-services li::before { content: "✓"; display: inline-flex; justify-content: center; align-items: center; width: 10px; height: 10px; border: 1px solid var(--yellow); border-radius: 50%; color: var(--yellow); font-size: 7px; }
  .pill-offer { left: 18px; top: 460px; color: var(--white); font-size: 15px; font-style: italic; }
  .discount-band { left: 0; top: 487px; width: 474px; height: 40px; background: var(--yellow); color: var(--black); font-size: 19px; font-style: italic; font-weight: 600; line-height: 40px; padding-left: 16px; }
  .septic-web { left: 18px; top: 553px; color: var(--white); font-size: 19px; font-weight: 600; }
  .social-dots { left: 362px; top: 545px; width: 64px; display: grid; grid-template-columns: repeat(3, 16px); gap: 6px 8px; }
  .social-dots i { width: 16px; height: 16px; border: 1.5px solid var(--white); border-radius: 50%; }
  .mail-return { left: 493px; top: 45px; font-family: var(--condensed); font-size: 12px; line-height: 17px; color: var(--black); }
  .flag-drape { left: 650px; top: 0; width: 250px; height: 200px; background: linear-gradient(120deg, #ffffff 0%, #c8102e 25%, #ffffff 40%, #c8102e 55%, #1f2f6e 75%, #1f2f6e 100%); clip-path: polygon(0 0, 100% 0, 100% 100%, 80% 72%, 40% 60%, 12% 35%); }
  .indicia { left: 783px; top: 38px; width: 78px; height: 68px; background: var(--white); border: 1px solid var(--black); font-family: var(--sans); font-size: 10px; line-height: 12px; text-align: center; padding-top: 3px; color: var(--black); }
  .indicia b { display: block; }
  .address-box { left: 613px; top: 253px; width: 250px; height: 100px; border: 1px solid #555; font-family: var(--sans); color: var(--black); }
  .address-box .route { position: absolute; right: 18px; top: 14px; font-size: 11px; }
  .address-box .to { position: absolute; left: 17px; top: 48px; font-size: 15px; line-height: 17px; }
  .back-phone { left: 515px; top: 495px; font-size: 46px; font-weight: 700; color: var(--black); display: flex; align-items: center; gap: 6px; }
  .back-phone svg { width: 34px; height: 34px; fill: var(--black); }
  .back-tag { left: 536px; top: 555px; font-size: 20px; font-style: italic; color: var(--black); }
</style>
</head>
<body>
<div class="sheet">

  <!-- Trash & roll-off side -->
  <section class="card-slot front">
    <div class="card">
      <div class="abs header"></div>
      <div class="abs brand-mark"></div>
      <h1 class="abs brand-name">Copper Vale<br>Waste Solutions</h1>
      <div class="abs years-seal"><span class="num">25</span><span class="lbl">YEARS</span></div>
      <div class="abs tagline">
        <h2>We don't talk trash, We talk solutions</h2>
        <p>Copper Vale Waste Solutions is a family owned<br>and operated business that started with<br>one truck and a dream...</p>
      </div>
      <div class="abs rule-top"></div>
      <div class="photo truck-photo" role="img" aria-label="Black and yellow garbage truck with company lettering"></div>
      <p class="abs se-habla">Se Habla Español</p>
      <div class="abs service-rail"></div>
      <div class="photo service-photo cans" role="img" aria-label="Black residential trash cans at a curb"></div>
      <p class="abs service-label l1">Residential Trash Removal</p>
      <div class="photo service-photo small-bin" role="img" aria-label="Small yellow 2 yard dumpster"></div>
      <p class="abs service-label l2">2yd Dumpsters</p>
      <div class="photo service-photo roll-off" role="img" aria-label="Black roll off dumpster at a build site"></div>
      <p class="abs service-label l3">Roll Off Dumpster</p>
      <div class="abs promo-band"></div>
      <div class="photo spokesman" role="img" aria-label="Smiling man in shirt and tie giving two thumbs up"></div>
      <div class="abs promo-copy">
        <p class="offer">Call for Start Up Specials, Military,<br>Senior, &amp; Clergy Discounts</p>
        <p class="local">Support Locally Owned &amp;<br>Operated Businesses!<br>Not Wolves in Sheep's Clothing!</p>
      </div>
      <p class="abs front-phone">
        <svg viewBox="0 0 24 24" aria-hidden="true"><path d="M6.6 10.8a15.1 15.1 0 0 0 6.6 6.6l2.2-2.2c.3-.3.7-.4 1-.2 1.1.4 2.3.6 3.6.6.6 0 1 .4 1 1V20c0 .6-.4 1-1 1A17 17 0 0 1 3 4c0-.6.4-1 1-1h3.5c.6 0 1 .4 1 1 0 1.3.2 2.5.6 3.6.1.3 0 .7-.2 1z"/></svg>
        (555)010-0189
      </p>
      <p class="abs front-web">www.coppervalewaste.example</p>
      <div class="abs ratings">
        <div class="rating"><span class="name">Searchly</span><span class="stars">★★★★★</span></div>
        <div class="rating"><span class="name"><i></i>Marla's roster</span><span class="stars">★★★★★</span></div>
        <div class="rating"><span class="name">chatterpage</span><span class="stars">★★★★★</span></div>
      </div>
      <div class="abs perks">
        <span>No Administration Fees</span>
        <span>No Contracts</span>
        <span>No Hidden Fees</span>
        <span>No Fuel Surcharges</span>
        <span>Online Billing or Billing Made Simple.</span>
      </div>
    </div>
  </section>

  <!-- Septic side -->
  <section class="card-slot back">
    <div class="card">
      <svg class="abs panel-shape" viewBox="0 0 520 600" aria-hidden="true">
        <path d="M0 0 H458 Q515 300 452 600 H0 Z" fill="#fbed22"/>
        <path d="M0 0 H440 Q497 300 436 600 H0 Z" fill="#000"/>
      </svg>
      <div class="abs septic-mark"></div>
      <h1 class="abs septic-name">Copper Vale<br>Septic</h1>
      <div class="abs emergency"><span class="big">24/7</span><span class="small">Emergency</span><span class="small">Services</span><span class="small">Available</span></div>
      <p class="abs estimate-band"><em>Let us do the dirty work!</em>Free Over the Phone Estimate!</p>
      <div class="photo septic-truck" role="img" aria-label="Yellow pump truck with black septic tank"></div>
      <p class="abs se-habla">Se Habla Español</p>
      <div class="photo thumb dig" role="img" aria-label="Worker with hose at an open septic lid"></div>
      <div class="photo thumb camera" role="img" aria-label="Septic camera snaking equipment"></div>
      <div class="photo thumb pills" role="img" aria-label="Boxes of septic pills"></div>
      <p class="abs septic-intro">Our team will immediately respond to your septic needs. We will work hard to complete your septic project with the utmost professionalism.</p>
      <ul class="abs septic-services">
        <li>Electronic tank location services</li>
        <li>Emergency septic repairs</li>
        <li>Camera snaking</li>
        <li>Real estate septic inspections.</li>
      </ul>
      <p class="abs pill-offer">12 month supply of Septic pills - 1 box for $55 or two for $95.</p>
      <p class="abs discount-band">Military, Senior, Clergy &amp; Seasonal Discounts</p>
      <p class="abs septic-web">www.coppervaleseptic.example</p>
      <div class="abs social-dots"><i></i><i></i><i></i><i></i><i></i><i></i></div>

      <p class="abs mail-return">Reach us by US Mail:<br>Copper Vale Waste Solutions<br>P.O. Box 214, Redfield, TX 75990<br>or Email: coppervaleseptic@mailhub.example</p>
      <div class="photo flag-drape" role="img" aria-label="Waving American flag"></div>
      <div class="abs indicia">PRSRT STD<br>ECRWSS<br>U.S. Postage<b>PAID</b>QRPX RETAIL</div>
      <div class="abs address-box">
        <span class="route">*****************ECRWSS****</span>
        <span class="to">Local<br>Postal Customer</span>
      </div>
      <p class="abs back-phone">
        <svg viewBox="0 0 24 24" aria-hidden="true"><path d="M6.6 10.8a15.1 15.1 0 0 0 6.6 6.6l2.2-2.2c.3-.3.7-.4 1-.2 1.1.4 2.3.6 3.6.6.6 0 1 .4 1 1V20c0 .6-.4 1-1 1A17 17 0 0 1 3 4c0-.6.4-1 1-1h3.5c.6 0 1 .4 1 1 0 1.3.2 2.5.6 3.6.1.3 0 .7-.2 1z"/></svg>
        555-010-0189
      </p>
      <p class="abs back-tag">Locally Owned &amp; Family Operated</p>
    </div>
  </section>

</div>
</body>
</html>
```